依頼詳細
起業をしようと思っているが
具体的にはどのようにしていいのかわからない方向けに
比較的安価でセミナーを開催しようと考えています。

希望しては、信頼感とフレンドリーさを感じられるサイトデザインを
提案していただければ幸いです。

参考として他社で気に入っているサイトは下記になります。
http://www.mirevo-kaigi.example/kanyu/yutai.html?ref=QZ7pLm4TxR2vNk8WdYs3HaBfE

また文章部分については自分でも考えますので
「******」などの伏せ字にしていただいても結構です。

たたき台として案をエクセルファイルにまとめまてあります。
必ずしもエクセルにある文章通りにしたりする必要はなく
構成を変えていただいたり、キャッチコピーを変えるなど
むしろしていただければ幸いです。
文章や構成などをうまく編集していただいた方には
万が一、当選しなくても、別に参加賞などで対応させていただきます。

今回はデザインのみでコーディングは不要です。
皆様、
非常に素晴らしい力作をご提案いただきありがとうございます。

まだ
提案予約をしていただいていますが
提出ができていない方がいらっしゃるため
期限を少し伸ばしたいと思います。

引き続きすばらしい作品をお待ちしております。
こちらのサイトの姉妹サイトで
簡単なTOPページの画像修正を
新規のTOBIRASの案件として依頼中です。

もしご興味のある人がいましたらば
ぜひご参加のほどよろしくお願い致します。

http://www.tobiras-works.example/job/view/527394
皆様、ご応募ありがとうございます。
これから選考に入らせていただきます。

このあと修正の可否などお伺いすることもあるかと思いますが
可能であればご返信いただければ幸いです。

1週間程度で最終的な採択をさせていただくつもりです。
それではよろしくお願い致します。

デザイン性が高く
ファーストビューで当事務所がお客様に伝えたいことを
的確に表現していただいた点

提案してくださいましたランサーの皆様
多くの素晴らしいデザインを提案していただいてありがとうございました。
また今後もデザインを発注することがあると思いますので
その際はどうぞよろしくお願い致します。

```html
<!DOCTYPE html>
<html lang="ja">
<head>
<meta charset="utf-8">
<title>起業・独立セミナー｜森川啓介公認会計士事務所</title>
<link href="https://fonts.googleapis.com/css2?family=Noto+Sans+JP:wght@400;500;700;900&family=Noto+Serif+JP:wght@500;700;900&display=swap" rel="stylesheet">
<style>
:root{
  --navy:#0d3b6e;
  --blue:#1f6fb3;
  --blue-light:#5fa7dc;
  --band-top:#4f9fd8;
  --band-bottom:#1d5f9e;
  --orange:#f29a18;
  --orange-light:#fbc34a;
  --red:#d9251d;
  --green:#3c9a3a;
  --green-light:#8cc63f;
  --cyan:#e6f3fb;
  --text:#222;
  --gray:#d9d9d9;
  --line:#9fb8cc;
  --cream:#fff7e2;
}
*{box-sizing:border-box;margin:0;padding:0}
html,body{width:1200px;height:4892px;overflow:hidden}
body{position:relative;background:#f4f4f4;font-family:"Noto Sans JP",sans-serif;color:var(--text)}
.page{position:absolute;left:40px;top:0;width:1120px;height:4892px;background:#fff}
.abs{position:absolute}

/* header */
.site-header{left:0;top:0;width:1120px;height:56px;background:#fff;border-bottom:1px solid #ddd}
.firm-name{left:16px;top:12px;font-family:"Noto Serif JP",serif;font-weight:700;font-size:26px;color:var(--navy)}
.phone{right:16px;top:4px;display:flex;align-items:center;gap:8px;font-size:40px;font-weight:700;color:var(--navy);line-height:48px}
.global-nav{left:0;top:56px;width:1120px;height:36px;background:linear-gradient(#f5f5f5,#d8d8d8);display:flex;border-bottom:1px solid #bbb}
.global-nav span{flex:1;text-align:center;font-size:21px;font-weight:500;line-height:36px;border-right:1px solid #aaa}

/* hero */
.hero{left:0;top:92px;width:1120px;height:212px;background:linear-gradient(135deg,#0f4c8c 0%,#2a7fc7 55%,#bfe0f5 100%)}
.hero-title{left:40px;top:10px;font-size:70px;font-weight:900;color:#fff;letter-spacing:4px;text-shadow:3px 3px 0 var(--navy)}
.hero-sub{left:60px;top:96px;font-size:26px;font-weight:700;color:#fff}
.hero-worry{left:60px;top:134px;font-size:22px;font-weight:700;color:#ffe34d}
.hero-list{left:80px;top:160px;list-style:none;font-size:17px;color:#fff;line-height:16px}
.hero-list li::before{content:"✔ ";color:#ffe34d}
.hero-photo{right:0;top:0;width:420px;height:212px;background:linear-gradient(90deg,rgba(255,255,255,0),#e9f2f9 30%,#cfd9e3)}

/* headline & arrow */
.lead{left:0;top:362px;width:1120px;text-align:center;font-size:56px;font-weight:900;color:var(--orange);text-shadow:2px 2px 0 #fff3c4}
.arrow{left:300px;top:440px}

/* band */
.band{left:0;width:1120px;height:80px;background:linear-gradient(var(--band-top),var(--band-bottom));color:#fff;font-size:44px;font-weight:700;text-align:center;line-height:80px;letter-spacing:4px;border-top:3px solid #bfe2f7}

/* solution */
.sol-box{border:4px solid var(--blue-light);border-radius:16px;background:#fff;padding:0 0 14px}
.sol-head{background:linear-gradient(var(--green-light),var(--green));color:#fff8a8;font-size:30px;font-weight:900;text-align:center;padding:10px 0;border-radius:12px 12px 0 0}
.sol-head.blue{background:linear-gradient(#6cb7e6,var(--blue));}
.sol-sub{font-size:30px;font-weight:900;color:var(--navy);padding:12px 24px 4px}
.sol-text{font-size:24px;line-height:38px;padding:4px 24px}

/* merit */
.merit{left:40px;top:1500px;width:1040px;height:380px;background:linear-gradient(var(--orange-light),var(--orange));border-radius:24px}
.merit-title{left:0;top:14px;width:1040px;text-align:center;font-size:60px;font-weight:900;color:var(--red);text-shadow:2px 2px 0 #fff3c4}
.merit-band{left:0;top:100px;width:1040px;height:68px;background:linear-gradient(#7a5a2e,#4a3214);color:#fff;font-size:44px;font-weight:700;text-align:center;line-height:68px;letter-spacing:6px}
.merit-body{left:24px;top:182px;width:992px;font-size:28px;font-weight:500;line-height:44px;color:#fff}
.merit-body strong{color:#fff7a1;font-size:30px}

/* voice */
.voice{width:300px}
.voice-company{font-size:18px;height:22px}
.voice-name{font-size:20px;margin-bottom:10px}
.voice-photo{width:280px;height:310px;background:var(--gray)}
.voice-title{font-size:20px;margin-top:16px;border-bottom:1px solid #aaa;padding-bottom:4px}
.voice-text{font-size:18px;line-height:30px;margin-top:6px}

/* lecture */
.topic{width:220px;height:100px;border-radius:16px;display:flex;align-items:center;justify-content:center;text-align:center;font-size:28px;font-weight:900;line-height:34px}
.topic.orange{background:#fde1a0;border:4px solid var(--orange);color:#c74d00}
.topic.cyan{background:#d6eefc;border:4px solid var(--blue-light);color:var(--navy)}
.topic.purple{background:#eadff5;border:4px solid #a98ad0;color:#5b3592}
.topic.pink{background:#fbdde8;border:4px solid #e78fb0;color:#b42a5f}
.fee-note{left:180px;top:2976px;font-size:18px;color:var(--navy)}
.fee{left:60px;top:2996px;display:flex;align-items:baseline;gap:24px;color:var(--red);font-weight:900}
.fee .label{font-size:52px;background:#fff0a0;padding:0 10px}
.fee .price{font-size:72px}
.lecture-photo{left:600px;top:2760px;width:460px;height:320px;background:linear-gradient(#f4f8fb,#d7e2ea)}

/* profile */
.profile{left:40px;top:3272px;width:1040px;height:220px;border:3px solid var(--line);background:#fff}
.profile-name{left:40px;top:20px;font-family:"Noto Serif JP",serif;font-size:60px;font-weight:900;letter-spacing:20px}
.profile-label{left:40px;top:106px;font-family:"Noto Serif JP",serif;font-size:22px;font-weight:700}
.profile-text{left:40px;top:138px;width:720px;font-family:"Noto Serif JP",serif;font-size:16px;line-height:22px}
.profile-photo{left:800px;top:10px;width:200px;height:200px;background:linear-gradient(#d9e6ef,#5b7088)}

/* qa */
.qa{width:320px;height:300px;border:3px solid var(--line);border-radius:16px;background:#fff;padding:24px 20px}
.qa p{display:flex;align-items:center;gap:14px;font-size:30px;font-weight:700;letter-spacing:2px;margin-bottom:80px}
.qa .mark{width:44px;height:44px;border-radius:50%;background:var(--blue);color:#fff;font-size:26px;display:flex;align-items:center;justify-content:center}
.qa .mark.a{background:var(--orange)}

/* form */
.form-note{left:40px;top:4064px;font-size:18px;font-weight:700}
.form-table{left:40px;top:4092px;width:1040px;border-collapse:collapse;font-size:20px}
.form-table th{width:160px;background:var(--cyan);border:2px solid var(--line);text-align:left;padding:0 16px;font-weight:700}
.form-table td{border:2px solid var(--line);padding:8px 16px}
.req{color:var(--red)}
.date-row{display:flex;align-items:center;gap:20px;line-height:34px}
.radio{width:16px;height:16px;border:2px solid #666;border-radius:50%}
.full{background:var(--red);color:#fff;font-weight:700;padding:0 10px;font-size:18px}
.input{height:36px;border:1px solid #bbb;width:520px}
.submit{left:340px;top:4448px;width:440px;height:76px;background:linear-gradient(var(--orange-light),var(--orange));border-radius:10px;color:#fff;font-size:44px;font-weight:900;text-align:center;line-height:76px;letter-spacing:8px;text-shadow:1px 1px 0 #b4600a}

/* footer */
.site-footer{left:-40px;top:4600px;width:1200px;height:292px;background:linear-gradient(#1f5284,#0c2f56)}
.footer-text{left:80px;top:60px;font-family:"Noto Serif JP",serif;color:#fff;font-size:34px;line-height:56px}
</style>
</head>
<body>
<div class="page">

  <header class="site-header abs">
    <div class="firm-name abs">森川啓介公認会計士事務所</div>
    <div class="phone abs">
      <svg width="44" height="40" viewBox="0 0 44 40"><path d="M6 14 Q22 0 38 14 L34 20 L28 16 L28 12 Q22 9 16 12 L16 16 L10 20 Z" fill="#0d3b6e"/><rect x="10" y="22" width="24" height="16" rx="3" fill="#0d3b6e"/><circle cx="22" cy="30" r="4" fill="#fff"/></svg>
      03-5550-0142
    </div>
  </header>

  <nav class="global-nav abs">
    <span>ホーム</span><span>参加者の声</span><span>講義内容</span><span>講師略歴</span><span>よくあるQ&amp;A</span><span style="border-right:none">申し込みフォーム</span>
  </nav>

  <section class="hero abs">
    <div class="hero-photo abs" role="img" aria-label="ビジネスパーソンの男女の写真"></div>
    <h1 class="hero-title abs">起業・独立セミナー</h1>
    <p class="hero-sub abs">〜起業を志す方の学びの場、交流の場〜</p>
    <p class="hero-worry abs">こんな悩みはありませんか？</p>
    <ul class="hero-list abs">
      <li>起業をしたいが何をはじめたらいいかわからない</li>
      <li>融資？銀行からお金を借りるのに不安がある</li>
      <li>起業について相談する時間がない</li>
    </ul>
  </section>

  <p class="lead abs">このセミナーで悩みを解決しませんか？</p>
  <svg class="arrow abs" width="520" height="260" viewBox="0 0 520 260">
    <defs><linearGradient id="arrowFill" x1="0" y1="0" x2="0" y2="1"><stop offset="0" stop-color="#f04a3a"/><stop offset="1" stop-color="#b3140e"/></linearGradient></defs>
    <polygon points="130,0 390,0 390,110 520,110 260,260 0,110 130,110" fill="url(#arrowFill)"/>
  </svg>

  <h2 class="band abs" style="top:760px">解決方法</h2>

  <div class="sol-box abs" style="left:40px;top:880px;width:500px;height:270px">
    <div class="sol-head">基礎からわかる丁寧な講義</div>
    <div class="sol-sub">基礎の基礎から講義します</div>
    <p class="sol-text">さらに助成金などお得な情報や<br>知らないと損をする税金についても!</p>
  </div>
  <div class="sol-box abs" style="left:40px;top:1180px;width:500px;height:290px">
    <div class="sol-head" style="line-height:36px">わからないことは<br>いつでも質問できる体制</div>
    <div class="sol-sub">少人数制</div>
    <p class="sol-text">10名までの少人数制なので気軽に<br>講師に質問できるのもポイント<br>起業の仲間ができる</p>
  </div>
  <div class="sol-box abs" style="left:580px;top:880px;width:500px;height:500px">
    <div class="sol-head blue">本当の起業ノウハウ</div>
    <div class="sol-sub">専門家による価値の講義内容</div>
    <p class="sol-text">MBAによる事業計画の立案方法<br>メガバンク出身者による融資の話<br>税理士による税金対策</p>
    <div class="sol-sub" style="color:#3c9a3a">100社以上の起業支援実績</div>
    <p class="sol-text">教科書的な話だけではなく、<br>実践的な知識わからないところは<br>いつでも質問できる体制</p>
  </div>

  <section class="merit abs">
    <p class="merit-title abs">最大のメリットはここ</p>
    <p class="merit-band abs">起業の仲間ができる</p>
    <p class="merit-body abs"><strong>起業を志す仲間がいるのは心強いもの</strong><br>同じ時期に起業を志しているので、同じ悩みにぶつかっていることも<br>またすでに同じ悩みにぶつかって解決していることも！<br>さらに飲み会も企画しています。</p>
  </section>

  <h2 class="band abs" style="top:1912px">参加者の声</h2>
  <div class="voice abs" style="left:40px;top:2030px">
    <p class="voice-company">株式会社＊＊＊</p><p class="voice-name">宮城さん</p>
    <div class="voice-photo" role="img" aria-label="参加者の写真"></div>
    <p class="voice-title">この起業セミナーに参加して</p>
    <p class="voice-text">基礎から丁寧に学べました。<br>融資の不安が解消しました。<br>仲間ができて心強いです。</p>
  </div>
  <div class="voice abs" style="left:410px;top:2030px">
    <p class="voice-company"></p><p class="voice-name">西田さん</p>
    <div class="voice-photo" role="img" aria-label="参加者の写真"></div>
    <p class="voice-title">この起業セミナーに参加して</p>
    <p class="voice-text">事業計画の立て方が明確に。<br>質問しやすい雰囲気でした。<br>次回も参加したいです。</p>
  </div>
  <div class="voice abs" style="left:780px;top:2030px">
    <p class="voice-company"></p><p class="voice-name">大野さん</p>
    <div class="voice-photo" role="img" aria-label="参加者の写真"></div>
    <p class="voice-title">この起業セミナーに参加して</p>
    <p class="voice-text">税金の知識が身につきました。<br>具体的で分かりやすいです。<br>一歩踏み出せました。</p>
  </div>

  <h2 class="band abs" style="top:2632px">講義内容</h2>
  <div class="topic orange abs" style="left:60px;top:2750px">起業の方法</div>
  <div class="topic cyan abs" style="left:310px;top:2750px">助成金の<br>獲得方法</div>
  <div class="topic purple abs" style="left:60px;top:2866px">融資のための<br>ノウハウ</div>
  <div class="topic pink abs" style="left:310px;top:2866px">懇親会<br>(希望者のみ)</div>
  <p class="fee-note abs">講義後の飲み会は別途実費負担</p>
  <div class="fee abs"><span class="label">料金</span><span class="price">2,000円</span></div>
  <div class="lecture-photo abs" role="img" aria-label="講義を受けるビジネスパーソンの写真"></div>

  <h2 class="band abs" style="top:3180px">講師略歴</h2>
  <section class="profile abs">
    <p class="profile-name abs">森川 啓介</p>
    <p class="profile-label abs">略歴</p>
    <p class="profile-text abs">青葉学院大学大学院（MBA）卒業<br>公認会計士・税理士<br>監査法人、外資系コンサルティング会社、ひかり銀行を経て独立<br>起業に特化したコンサルティングおよび会計事務所を開業</p>
    <div class="profile-photo abs" role="img" aria-label="講師の写真"></div>
  </section>

  <h2 class="band abs" style="top:3500px">よくあるQ&amp;A</h2>
  <div class="qa abs" style="left:40px;top:3620px"><p><span class="mark">Q</span>＊＊＊＊＊＊＊</p><p><span class="mark a">A</span>＊＊＊＊＊＊＊</p></div>
  <div class="qa abs" style="left:400px;top:3620px"><p><span class="mark">Q</span>＊＊＊＊＊＊＊</p><p><span class="mark a">A</span>＊＊＊＊＊＊＊</p></div>
  <div class="qa abs" style="left:760px;top:3620px"><p><span class="mark">Q</span>＊＊＊＊＊＊＊</p><p><span class="mark a">A</span>＊＊＊＊＊＊＊</p></div>

  <h2 class="band abs" style="top:3960px">申し込みフォーム</h2>
  <p class="form-note abs">下記<span class="req">※</span>印は入力必須となります。</p>
  <table class="form-table abs">
    <tr style="height:140px"><th><span class="req">※</span>日程</th><td>
      <div class="date-row"><span class="radio"></span>4/15（土）　16時〜　場所　東都商工会館<span class="full">満員御礼</span></div>
      <div class="date-row"><span class="radio"></span>4/29（土）　16時〜　場所　東都商工会館</div>
      <div class="date-row"><span class="radio"></span>5/10（土）　17時〜　場所　東都商工会館</div>
    </td></tr>
    <tr style="height:52px"><th><span class="req">※</span>お名前</th><td><div class="input"></div></td></tr>
    <tr style="height:52px"><th><span class="req">※</span>電話番号</th><td><div class="input"></div></td></tr>
    <tr style="height:52px"><th><span class="req">※</span>メールアドレス</th><td><div class="input"></div></td></tr>
    <tr style="height:80px"><th>その他</th><td><div class="input" style="height:60px;width:880px"></div></td></tr>
  </table>
  <div class="submit abs">申し込む</div>

  <footer class="site-footer abs">
    <p class="footer-text abs">運営会社<br>株式会社Bay Harbor Consulting<br>森川啓介公認会計士事務所</p>
  </footer>
</div>
</body>
</html>
```